Professional PowerPoint Template for Data Reports, Presentations

We are a small leadership coaching/consulting firm and would like to update our PowerPoint template that we use with our clients, who are typically mid-senior level company professionals. I've attached a sample Powerpoint as well as our branding guide. The cover page is what needs the most work - just doesn't look current/professional enough. We do want to keep the pages after that clean, with come color but enough space for text and graphics.
Target Market(s)
Senior mgmt and HR executives in small-mid sized companies
Font styles to use
Sans Serif
Requirements
Must have
- Professional
- Clean
- Tied to company color scheme/logo
Nice to have
- Our title pages don't usually have many words on them; we'd like a design that has a lot of color - probably still using mainly our blue but accented with other colors.
- Need simple but smart looking pages after cover with lot of space; mostly we have text on the slides. Currently this is often in bullet point style, but we could probably upgrade the options there.
Should not have
- Anything that looks like a marketing style, as we typically use these with our current clients to share results of data collected, project plans, etc.

```html
<!DOCTYPE html>
<html lang="en">
<head>
<meta charset="utf-8">
<title>Helmsway Company – Presentation Template</title>
<link href="https://fonts.googleapis.com/css2?family=Arimo:wght@400&family=Josefin+Sans:wght@600&display=swap" rel="stylesheet">
<style>
  :root{
    --brand-blue:#2c5a8f;
    --brand-navy:#15304f;
    --panel-grey:#ececec;
    --teal:#7ab8ae;
    --sky:#cfe3ef;
    --coral:#ee7f4e;
    --white:#ffffff;
    --stage:#000000;
  }
  *{margin:0;padding:0;box-sizing:border-box}
  html,body{width:813px;height:1200px;overflow:hidden;background:var(--stage)}
  body{position:relative;font-family:"Arimo",Arial,sans-serif}
  .slide{position:absolute;background:var(--white);overflow:hidden}
  .slide--cover{left:34px;top:30px;width:746px;height:560px}
  .slide--content{left:32px;top:600px;width:747px;height:560px}
  .slide svg.art{position:absolute;inset:0;width:100%;height:100%}
  .contact{position:absolute;color:var(--white);font-size:13.5px;white-space:nowrap;line-height:1}
  .icon{position:absolute;width:16px;height:16px}
  .wordmark{
    position:absolute;left:53px;top:420px;
    font-family:"Josefin Sans",Arial,sans-serif;font-weight:600;
    font-size:48px;letter-spacing:4px;color:var(--brand-blue);line-height:1;
    white-space:nowrap;
  }
  .footer-bar{
    position:absolute;left:109px;top:530px;height:30px;
    display:flex;align-items:center;gap:20px;
    color:var(--white);font-size:12.5px;white-space:nowrap;line-height:1;
  }
  .footer-item{display:flex;align-items:center;gap:6px}
  .footer-item svg{width:15px;height:15px;flex:none}
  .footer-name{
    font-family:"Josefin Sans",Arial,sans-serif;font-weight:600;
    font-size:12px;letter-spacing:2px;margin-left:6px;
  }
</style>
</head>
<body>

<section class="slide slide--cover">
  <svg class="art" viewBox="0 0 932 699" preserveAspectRatio="none" aria-hidden="true">
    <defs>
      <linearGradient id="panelShade" x1="0" x2="1" y1="0" y2="0">
        <stop offset="0" stop-color="#2c5a8f"/>
        <stop offset="0.08" stop-color="#9fb1c7"/>
        <stop offset="0.16" stop-color="#e2e4e8"/>
        <stop offset="1" stop-color="#ececec"/>
      </linearGradient>
      <linearGradient id="baseWave" x1="0" x2="1" y1="0" y2="0">
        <stop offset="0" stop-color="#cfe3ef"/>
        <stop offset="0.55" stop-color="#9cc8c6"/>
        <stop offset="0.8" stop-color="#7ab8ae"/>
        <stop offset="1" stop-color="#7ab8ae"/>
      </linearGradient>
      <linearGradient id="coralWave" x1="0" x2="1" y1="0" y2="1">
        <stop offset="0" stop-color="#7ab8ae" stop-opacity="0"/>
        <stop offset="0.55" stop-color="#ee7f4e" stop-opacity="0.8"/>
        <stop offset="1" stop-color="#ee7f4e"/>
      </linearGradient>
    </defs>
    <path d="M0 0 H450 C470 200 540 260 535 350 C530 450 440 560 465 699 H0 Z" fill="url(#panelShade)"/>
    <path d="M450 64 C470 200 540 260 535 350 C530 450 440 560 465 675" fill="none" stroke="var(--brand-navy)" stroke-width="4"/>
    <path d="M0 578 Q220 665 480 672 L0 699 Z" fill="var(--brand-blue)"/>
    <path d="M0 640 Q160 678 480 668 Q650 660 720 628 Q800 585 860 586 Q900 588 932 600 V699 H0 Z" fill="url(#baseWave)"/>
    <path d="M520 699 Q700 690 760 650 Q830 605 932 625 V699 Z" fill="url(#coralWave)"/>
    <path d="M0 0 H932 V22 Q932 64 890 64 H42 Q0 64 0 22 Z" fill="var(--brand-navy)"/>
    <path d="M0 0 H932 V18 Q932 60 890 60 H42 Q0 60 0 18 Z" fill="var(--brand-blue)"/>
  </svg>

  <span class="contact" style="left:98px;top:11px">© Helmsway Company</span>
  <svg class="icon" style="left:80px;top:25px" viewBox="0 0 16 16" aria-hidden="true"><circle cx="8" cy="8" r="8" fill="#15304f"/><path d="M4 8.5 L8 4.5 L12 8.5 M5.5 7.5 V11.5 H10.5 V7.5" fill="none" stroke="#fff" stroke-width="1.4"/></svg>
  <span class="contact" style="left:99px;top:27px">PO Box 48, Linden, MA, 01555</span>
  <svg class="icon" style="left:335px;top:25px" viewBox="0 0 16 16" aria-hidden="true"><circle cx="8" cy="8" r="8" fill="#ee7f4e"/><circle cx="8" cy="8" r="4.5" fill="none" stroke="#fff" stroke-width="1"/><path d="M3.5 8 H12.5 M8 3.5 V12.5" stroke="#fff" stroke-width="1"/></svg>
  <span class="contact" style="left:357px;top:27px">www.helmswaycompany.com</span>
  <svg class="icon" style="left:553px;top:25px" viewBox="0 0 16 16" aria-hidden="true"><circle cx="8" cy="8" r="8" fill="#15304f"/><path d="M5 4.5 L6.5 4.3 L7.3 6.3 L6.4 7.1 Q7.4 9 8.9 9.6 L9.7 8.7 L11.7 9.5 L11.5 11 Q8.5 11.6 6.4 9.6 Q4.4 7.5 5 4.5 Z" fill="#fff"/></svg>
  <span class="contact" style="left:576px;top:27px">555-014-2276</span>

  <div class="wordmark">HELMSWAY</div>
</section>

<section class="slide slide--content">
  <svg class="art" viewBox="0 0 747 560" preserveAspectRatio="none" aria-hidden="true">
    <path d="M0 560 V556 Q0 528 30 528 H717 Q747 528 747 556 V560 Z" fill="var(--brand-navy)"/>
    <path d="M0 560 V558 Q0 530 30 530 H717 Q747 530 747 558 V560 Z" fill="var(--brand-blue)"/>
  </svg>
  <div class="footer-bar">
    <span class="footer-item">© Helmsway Company</span>
    <span class="footer-item">
      <svg viewBox="0 0 16 16" aria-hidden="true"><circle cx="8" cy="8" r="8" fill="#ee7f4e"/><circle cx="8" cy="8" r="4.5" fill="none" stroke="#fff" stroke-width="1"/><path d="M3.5 8 H12.5 M8 3.5 V12.5" stroke="#fff" stroke-width="1"/></svg>
      www.helmswaycompany.com
    </span>
    <span class="footer-item">
      <svg viewBox="0 0 16 16" aria-hidden="true"><circle cx="8" cy="8" r="8" fill="#15304f"/><path d="M5 4.5 L6.5 4.3 L7.3 6.3 L6.4 7.1 Q7.4 9 8.9 9.6 L9.7 8.7 L11.7 9.5 L11.5 11 Q8.5 11.6 6.4 9.6 Q4.4 7.5 5 4.5 Z" fill="#fff"/></svg>
      555-014-2276
    </span>
    <span class="footer-name">HELMSWAY</span>
  </div>
</section>

</body>
</html>
```